Business card, Letterhead and envelope design
Create a business card, letterhead and envelope design for Velmira Solutions
Professional
name
title
address
email@velmira-example.com
www.velmirasolutions-example.com
logo and font
Trifold brochure design we have for inspiration of design. This is for reference only.

```html
<!DOCTYPE html>
<html lang="en">
<head>
<meta charset="utf-8">
<title>Velmira Solutions — Stationery Set</title>
<link href="https://fonts.googleapis.com/css2?family=Poppins:wght@600&family=Open+Sans:wght@400;600&display=swap" rel="stylesheet">
<style>
  :root{
    --board:#a8a9ab;
    --paper:#ffffff;
    --ink:#3b3f45;
    --muted:#6c7076;
    --accent:#3a9ad9;
    --band-dark:#34373c;
    --fold:#c9cbce;
  }
  *{margin:0;padding:0;box-sizing:border-box}
  html,body{width:1200px;height:684px;overflow:hidden}
  body{background:var(--board);font-family:"Open Sans",Arial,sans-serif;color:var(--ink);position:relative}
  .sheet{position:absolute;background:var(--paper);box-shadow:0 1px 3px rgba(0,0,0,.25);overflow:hidden}

  .brand{display:flex;flex-direction:column;align-items:flex-start;font-family:"Poppins",Arial,sans-serif;font-weight:600;color:var(--ink);line-height:1.05}
  .brand-mark{background:var(--accent);display:block}
  .brand-name{display:block}

  .band{position:absolute;left:0;right:0;bottom:0;display:flex;color:#fff;font-size:6px;align-items:center}
  .band-web{background:var(--accent);height:100%;display:flex;align-items:center;padding-left:10px}
  .band-mail{background:var(--band-dark);flex:1;height:100%;display:flex;align-items:center;padding-left:10px}
  .contact-line{position:absolute;font-size:5.5px;color:var(--muted);white-space:nowrap}

  /* Letterhead */
  .letterhead{left:190px;top:14px;width:537px;height:651px}
  .letterhead .brand{position:absolute;left:24px;top:30px}
  .letterhead .brand-mark{width:38px;height:38px;margin-bottom:6px}
  .letterhead .brand-name{font-size:14px}
  .letterhead .contact-line{left:24px;bottom:33px}
  .letterhead .band{height:17px;bottom:8px}
  .letterhead .band-web{width:122px}

  /* Business card */
  .card{left:19px;top:281px;width:168px;height:98px}
  .card .brand{position:absolute;left:9px;top:8px;flex-direction:row;align-items:center;gap:5px}
  .card .brand-mark{width:18px;height:18px}
  .card .brand-name{font-size:9px}
  .card-person{position:absolute;left:9px;top:46px;font-size:5.5px;color:var(--accent);font-weight:600}
  .card-details{position:absolute;left:9px;top:57px;font-size:4.5px;color:var(--muted);line-height:1.5}
  .card .band{height:13px;font-size:4.5px}
  .card .band-web{width:78px;padding-left:6px}
  .card .band-mail{padding-left:6px}

  /* Envelope back */
  .envelope-back{left:646px;top:96px;width:540px;height:242px}
  .envelope-back svg{position:absolute;inset:0}
  .envelope-back .brand{position:absolute;left:248px;top:20px;align-items:center}
  .envelope-back .brand-mark{width:30px;height:30px;margin-bottom:3px}
  .envelope-back .brand-name{font-size:7px}

  /* Envelope front */
  .envelope-front{left:646px;top:377px;width:540px;height:247px}
  .envelope-front .brand{position:absolute;left:10px;top:26px}
  .envelope-front .brand-mark{width:44px;height:44px;margin-bottom:6px}
  .envelope-front .brand-name{font-size:15px}
  .envelope-front .contact-line{left:12px;bottom:34px}
  .envelope-front .band{height:15px;bottom:26px}
  .envelope-front .band-web{width:146px}
</style>
</head>
<body>

<section class="sheet letterhead" aria-label="Letterhead">
  <div class="brand"><span class="brand-mark"></span><span class="brand-name">Velmira<br>Solutions</span></div>
  <p class="contact-line">T: 555 010 2044 &nbsp;|&nbsp; F: 555 010 2045 &nbsp;|&nbsp; A: 18 Harbor Lane, Suite 4, Northfield, NY 10001</p>
  <div class="band"><span class="band-web">www.velmirasolutions-example.com</span><span class="band-mail">email@velmira-example.com</span></div>
</section>

<section class="sheet card" aria-label="Business card">
  <div class="brand"><span class="brand-mark"></span><span class="brand-name">Velmira<br>Solutions</span></div>
  <p class="card-person">Alex Marlow | CEO</p>
  <p class="card-details">18 Harbor Lane, Suite 4, Northfield, NY 10001<br>T: 555 010 2044 &nbsp; F: 555 010 2045</p>
  <div class="band"><span class="band-web">www.velmirasolutions-example.com</span><span class="band-mail">email@velmira-example.com</span></div>
</section>

<section class="sheet envelope-back" aria-label="Envelope back">
  <svg width="540" height="242" viewBox="0 0 540 242">
    <polyline points="0,1 200,72 340,72 540,1" fill="none" stroke="var(--fold)" stroke-width="1"/>
    <line x1="0" y1="241" x2="160" y2="160" stroke="var(--fold)" stroke-width="0.8"/>
    <line x1="540" y1="241" x2="380" y2="160" stroke="var(--fold)" stroke-width="0.8"/>
  </svg>
  <div class="brand"><span class="brand-mark"></span><span class="brand-name">Velmira Solutions</span></div>
</section>

<section class="sheet envelope-front" aria-label="Envelope front">
  <div class="brand"><span class="brand-mark"></span><span class="brand-name">Velmira<br>Solutions</span></div>
  <p class="contact-line">T: 555 010 2044 &nbsp;|&nbsp; F: 555 010 2045 &nbsp;|&nbsp; A: 18 Harbor Lane, Suite 4, Northfield, NY 10001</p>
  <div class="band"><span class="band-web">www.velmirasolutions-example.com</span><span class="band-mail">email@velmira-example.com</span></div>
</section>

</body>
</html>
```